Business Card Design Project

We need a Business Card for an Mechanical Engineering firm in Singapore. The design should be Modern & Technical looking, yet eye catching.

Our company deals in Cutting Tools & Machine Accessories for the Manufacturing Industries such as Oil & Gas, Aero Space, etc... For more information on our Company, you can either email me or view our website www.valtrion.com.sg.

We are trying to revamp our image to give our consumers a fresh new perspective to our company, so we welcome all ideas.

Industry/Entity Type

Business

Requirements
Must have
• Must incorporate New Company Logo into the card as shown in Uploaded file.

```html
<!DOCTYPE html>
<html lang="en">
<head>
<meta charset="utf-8">
<title>Valtrion Tools – Business Card</title>
<link rel="stylesheet" href="https://fonts.googleapis.com/css2?family=Carlito:wght@400;700&family=Lobster+Two:ital,wght@1,700&display=swap">
<style>
  :root {
    --card-bg: #ffffff;
    --ink: #4a0f2a;
    --brand: #9c1440;
  }
  * { margin: 0; padding: 0; box-sizing: border-box; }
  html, body {
    width: 709px;
    height: 1200px;
    overflow: hidden;
    background: var(--card-bg);
  }
  .card {
    position: relative;
    width: 709px;
    height: 1200px;
    background: var(--card-bg);
    font-family: "Carlito", "Calibri", sans-serif;
    color: var(--ink);
  }
  .brand {
    position: absolute;
    left: 53px;
    top: 250px;
    width: 600px;
    display: flex;
    align-items: center;
    justify-content: center;
    gap: 20px;
  }
  .brand-mark {
    width: 56px;
    height: 56px;
    border-radius: 50%;
    background: var(--brand);
    flex: none;
  }
  .brand-name {
    font-family: "Carlito", "Calibri", sans-serif;
    font-weight: 400;
    font-size: 72px;
    letter-spacing: 1px;
    color: var(--brand);
    line-height: 1;
  }
  .details {
    position: absolute;
    left: 78px;
    top: 470px;
    width: 600px;
  }
  .company-name {
    font-weight: 700;
    font-size: 45px;
    line-height: 1.2;
    margin-bottom: 6px;
  }
  .address, .contacts {
    font-size: 33px;
    line-height: 52px;
    font-style: normal;
  }
  .contacts { margin-top: 52px; }
  .contact-person {
    position: absolute;
    left: 78px;
    top: 1055px;
  }
  .contact-label {
    font-size: 25px;
    line-height: 1.2;
  }
  .contact-name {
    font-family: "Lobster Two", cursive;
    font-style: italic;
    font-weight: 700;
    font-size: 48px;
    line-height: 1.2;
  }
</style>
</head>
<body>
  <main class="card">
    <header class="brand">
      <span class="brand-name">VALTRION TOOLS</span>
      <span class="brand-mark" aria-hidden="true"></span>
    </header>

    <section class="details">
      <h1 class="company-name">Valtrion Tools Pte Ltd</h1>
      <address class="address">
        27 Kallang Crescent #03-12,<br>
        Norvale Industrial Centre,<br>
        Singapore 339418
      </address>
      <p class="contacts">
        Tel: 65-63920417<br>
        Fax: 65-63920418<br>
        Email: hello@valtrion.com.sg<br>
        Website: www.valtrion.com.sg
      </p>
    </section>

    <footer class="contact-person">
      <p class="contact-label">Contact Person</p>
      <p class="contact-name">Miranda</p>
    </footer>
  </main>
</body>
</html>
```